Charity auction mobile bidding site

Our charities can build their own event landing page to promote their silent auction fundraising event. We need a top menu, hero image with event title and desc, a register/login area, up to 4 content blocks and an auction listing of items in a grid dynamically created from their catalog. Currently we have this laid out in 100% width layers or stacks. It needs to be mobile friendly first. Examples include kvtrial.plq.example and lindvar.plq.example and gabscheck.plq.example We need to allow people to design nice sites instead of PalNook pages that look terrible.

Target Market(s)

Soccer moms and volunteers who feel like rockstars when they learn how to use chumwall or clipboardly. Not super savvy so less is more. Not overwhelming. Clean with whitespace and functional is what they want

Number of Pages Required

1 page

Font styles to use
Sans Serif

Colors

Designer to choose colors to be used in the design.

Requirements
Must have
• Nothing so tightly designed that it would look terrible if an organization loaded their own photos. This means the hero image could be landscape or portrait. When in doubt, keep it clean and simple. A one or two color palette
Nice to have
• A pop up concept for someone to log in when they choose to bid on an item in the preview.
Should not have
• Decorative fonts. Too many colors.

```html
<!DOCTYPE html>
<html lang="en">
<head>
<meta charset="utf-8">
<title>Event Page – Brighter Paths</title>
<link rel="stylesheet" href="https://fonts.googleapis.com/css2?family=Mulish:wght@300;400;600;700;800&display=swap">
<style>
:root{
  --accent:#fcc844;
  --ink:#3a3a3a;
  --muted:#8a8a8a;
  --line:#d9d9d9;
  --soft:#f2f2f2;
  --foot:#f5f5f5;
  --brand:#e58a3a;
  --link:#5b7bb4;
  --white:#ffffff;
}
*{box-sizing:border-box;margin:0;padding:0}
html,body{width:1200px;height:3106px;overflow:hidden}
body{font-family:'Mulish',sans-serif;color:var(--ink);background:var(--white);position:relative}
.abs{position:absolute}
.center{left:0;width:1200px;text-align:center}

/* nav */
.topnav{top:0;left:0;width:1200px;height:52px;background:var(--white);border-bottom:1px solid #eee}
.topnav a{position:absolute;top:20px;font-size:9px;font-weight:600;letter-spacing:.4px;color:var(--ink);text-decoration:none;transform:translateX(-50%)}
.topnav svg{position:absolute;top:20px}

/* hero */
.hero{top:52px;left:0;width:1200px;height:476px;background:linear-gradient(180deg,#7a5a3a 0%,#c88a4a 30%,#d79a55 50%,#8a7350 75%,#4e5a3e 100%)}
.hero-shade{top:52px;left:0;width:1200px;height:476px;background:radial-gradient(ellipse at 50% 30%,rgba(255,190,90,.45),rgba(0,0,0,.15) 70%)}
.brandmark{display:flex;align-items:center;justify-content:center;gap:8px}
.brandmark .dot{width:14px;height:14px;border-radius:50%;background:var(--brand)}
.brandmark span{font-size:22px;font-weight:600;color:var(--brand)}
.hero-title{top:279px;font-size:30px;font-weight:700;color:var(--white)}
.hero-desc{top:332px;left:380px;width:440px;text-align:center;font-size:12.5px;line-height:19.5px;color:var(--white)}
.btn{background:var(--accent);color:var(--white);font-size:8.5px;font-weight:700;letter-spacing:.5px;text-align:center;display:flex;align-items:center;justify-content:center}
.btn-outline{border:2px solid var(--line);color:var(--ink);background:var(--white);font-size:8.5px;font-weight:800;display:flex;align-items:center;justify-content:center}

/* welcome */
.welcome h2{font-size:17px;font-weight:600;color:var(--ink)}
.welcome p{font-size:11px;color:var(--muted);margin-top:7px}
.login-input{top:556px;left:493px;width:280px;height:30px;border:1px solid var(--line);font-size:7.5px;color:var(--muted);padding:10px 14px}

/* donate */
.donate-bg{top:616px;left:0;width:1200px;height:525px;background:linear-gradient(180deg,#9a7fb8 0%,#4a3a5e 40%,#2e2a3e 100%)}
.donate-card{top:655px;left:115px;width:945px;height:448px;background:var(--white)}
.section-title{font-size:25px;font-weight:600;color:var(--ink)}
.section-sub{font-size:11px;color:var(--muted)}
.form-head{font-size:10.5px;font-weight:600}
.lbl{font-size:7.5px;font-weight:600}
.field{height:31px;border:1px solid var(--line);background:var(--white)}

/* sponsors */
.badge{border-radius:2px}

/* auctions */
.auctions{top:1397px;left:0;width:1200px;height:828px;background:var(--soft)}
.lot{width:474px;height:77px;background:var(--white);box-shadow:0 1px 3px rgba(0,0,0,.05)}
.lot-photo{position:absolute;left:6px;top:6px;width:98px;height:60px;background:linear-gradient(135deg,#2a1a12,#6e3a22 55%,#b06a3a)}
.lot-tag{position:absolute;left:0;top:0;width:36px;height:16px;background:#4a4a4a;color:var(--white);font-size:8px;font-weight:800;padding:2px 3px;clip-path:polygon(0 0,100% 0,70% 100%,0 100%)}
.lot h3{position:absolute;left:117px;top:12px;font-size:14.5px;font-weight:800;color:var(--ink)}
.lot p{position:absolute;left:117px;top:32px;font-size:8.5px;color:#555}
.lot .start{position:absolute;left:117px;top:51px;width:91px;height:15px;font-size:7.5px}
.lot .value{position:absolute;left:214px;top:51px;width:92px;height:15px;border:1.5px solid #666;font-size:7.5px;font-weight:800}

/* event details */
.col h4{font-size:16px;font-weight:500;color:var(--ink);margin-bottom:9px}
.col p{font-size:11px;line-height:18.5px;color:#444}
.col b{font-weight:800}
.about p{line-height:20.5px}

/* footer */
.footer{top:2925px;left:0;width:1200px;height:181px;background:var(--foot)}
.social{display:flex;gap:10px}
.social span{display:flex;align-items:center;justify-content:center;width:28px;height:28px;background:#4e6ca0;color:var(--white);font-size:5px;font-weight:700}
</style>
</head>
<body>

<nav class="abs topnav">
  <a style="left:365px">LOGIN</a>
  <a style="left:474px">DONATE</a>
  <a style="left:594px">SPONSORS</a>
  <a style="left:719px">AUCTIONS</a>
  <a style="left:833px">EVENT</a>
  <svg style="left:1036px" width="10" height="10" viewBox="0 0 10 10"><circle cx="4" cy="4" r="3" fill="none" stroke="#333" stroke-width="1.3"/><line x1="6.3" y1="6.3" x2="9" y2="9" stroke="#333" stroke-width="1.3"/></svg>
  <svg style="left:1062px" width="10" height="10" viewBox="0 0 10 10"><path d="M5 1a3 3 0 0 0-3 3v3l-1 1h8l-1-1V4a3 3 0 0 0-3-3z" fill="#333"/><circle cx="5" cy="9.2" r="0.9" fill="#333"/></svg>
  <svg style="left:1089px" width="10" height="10" viewBox="0 0 10 10"><circle cx="5" cy="3" r="2.3" fill="#333"/><path d="M1 10c0-3 2-4 4-4s4 1 4 4z" fill="#333"/></svg>
</nav>

<section>
  <div class="abs hero" role="img" aria-label="Hero photo: two young children walking on a road at sunset"></div>
  <div class="abs hero-shade"></div>
  <div class="abs center brandmark" style="top:225px"><i class="dot"></i><span>Brighter Paths</span></div>
  <h1 class="abs center hero-title">YOUR EVENT TITLE</h1>
  <p class="abs hero-desc">Lorem ipsum dolor sit amet, consectetur adipisicing elit, sed do eiusmod tempor incididunt ut labore et dolore magna aliqua. Ut enim ad minim veniam, quis nostrud exercitation ullamco laboris nisi ut aliquip ex.</p>
  <div class="abs btn" style="left:538px;top:423px;width:125px;height:33px">VIEW AUCTION</div>
</section>

<section class="welcome">
  <div class="abs" style="left:162px;top:551px">
    <h2>Welcome to the event page</h2>
    <p>Please log in or register to bid on an auction item</p>
  </div>
  <div class="abs login-input">LOG IN : Enter Phone, Email or Bid number</div>
  <div class="abs btn" style="left:773px;top:555px;width:93px;height:31px">LOGIN</div>
  <div class="abs" style="left:884px;top:565px;font-size:12px;font-weight:700">OR</div>
  <div class="abs btn-outline" style="left:917px;top:555px;width:126px;height:31px">REGISTER TO BID</div>
</section>

<section>
  <div class="abs donate-bg" role="img" aria-label="Blurred photo of an evening gala crowd"></div>
  <div class="abs donate-card"></div>
  <h2 class="abs center section-title" style="top:682px">Donate an Item</h2>
  <p class="abs center section-sub" style="top:732px">Thank you for donating an item to our auction. Please fill in the form below for details.</p>
  <div class="abs center form-head" style="top:783px">ITEM DETAILS</div>
  <div class="abs lbl" style="left:165px;top:825px">ITEM NAME</div>
  <div class="abs field" style="left:240px;top:814px;width:346px"></div>
  <div class="abs lbl" style="left:601px;top:825px">DESCRIPTION</div>
  <div class="abs field" style="left:667px;top:814px;width:346px"></div>
  <div class="abs lbl" style="left:165px;top:869px">MARKET VALUE</div>
  <div class="abs field" style="left:240px;top:857px;width:346px"></div>
  <div class="abs lbl" style="left:601px;top:869px">EXCEPTION</div>
  <div class="abs field" style="left:667px;top:857px;width:346px"></div>
  <div class="abs center form-head" style="top:923px">YOUR DETAILS</div>
  <div class="abs lbl" style="left:165px;top:965px">YOUR NAME</div>
  <div class="abs field" style="left:240px;top:953px;width:346px"></div>
  <div class="abs lbl" style="left:605px;top:965px">YOUR EMAIL</div>
  <div class="abs field" style="left:667px;top:953px;width:346px"></div>
  <div class="abs lbl" style="left:165px;top:1008px">YOUR PHONE</div>
  <div class="abs field" style="left:240px;top:997px;width:346px"></div>
  <div class="abs lbl" style="left:618px;top:1008px">NOTES</div>
  <div class="abs field" style="left:667px;top:997px;width:346px"></div>
  <div class="abs btn" style="left:553px;top:1050px;width:93px;height:33px">SEND</div>
</section>

<section>
  <h2 class="abs center section-title" style="top:1166px">Sponsors</h2>
  <p class="abs center section-sub" style="top:1213px">Thank you to our generous sponsors!</p>
  <div class="abs badge" style="left:120px;top:1261px;width:83px;height:83px;border-radius:50%;background:#a0507a"></div>
  <div class="abs badge" style="left:226px;top:1279px;width:192px;height:48px;background:#6fb0b0"></div>
  <div class="abs badge" style="left:445px;top:1261px;width:99px;height:81px;background:#c8102e"></div>
  <div class="abs badge" style="left:582px;top:1268px;width:46px;height:68px;background:#1a1a1a"></div>
  <div class="abs badge" style="left:666px;top:1261px;width:119px;height:81px;background:#1e3f8a"></div>
  <div class="abs badge" style="left:820px;top:1266px;width:260px;height:68px;background:#1d3c78"></div>
</section>

<section>
  <div class="abs auctions"></div>
  <h2 class="abs center section-title" style="top:1449px">Auctions</h2>
  <p class="abs section-sub" style="left:380px;top:1497px;width:440px;text-align:center;line-height:15px">Lorem ipsum dolor sit amet, consectetur adipisicing elit, sed do eiusmod tempor incididunt ut labore et dolore magna aliqua. Ut enim ad minim veniam, quis</p>

  <div class="abs lot" style="left:115px;top:1570px"><div class="lot-photo" role="img" aria-label="Steak dinner plate"></div><div class="lot-tag">100</div><h3>STEAK DINNER</h3><p>Steak Dinner for 4 at ACME steakhouse. Excludes drinks &amp; gratuity cap of $150</p><div class="btn start">STARTING : $75</div><div class="value btn-outline">VALUE : $150</div></div>
  <div class="abs lot" style="left:615px;top:1570px"><div class="lot-photo" role="img" aria-label="Steak dinner plate"></div><div class="lot-tag">100</div><h3>STEAK DINNER</h3><p>Steak Dinner for 4 at ACME steakhouse. Excludes drinks &amp; gratuity cap of $150</p><div class="btn start">STARTING : $75</div><div class="value btn-outline">VALUE : $150</div></div>
  <div class="abs lot" style="left:115px;top:1659px"><div class="lot-photo" role="img" aria-label="Steak dinner plate"></div><div class="lot-tag">100</div><h3>STEAK DINNER</h3><p>Steak Dinner for 4 at ACME steakhouse. Excludes drinks &amp; gratuity cap of $150</p><div class="btn start">STARTING : $75</div><div class="value btn-outline">VALUE : $150</div></div>
  <div class="abs lot" style="left:615px;top:1659px"><div class="lot-photo" role="img" aria-label="Steak dinner plate"></div><div class="lot-tag">100</div><h3>STEAK DINNER</h3><p>Steak Dinner for 4 at ACME steakhouse. Excludes drinks &amp; gratuity cap of $150</p><div class="btn start">STARTING : $75</div><div class="value btn-outline">VALUE : $150</div></div>
  <div class="abs lot" style="left:115px;top:1748px"><div class="lot-photo" role="img" aria-label="Steak dinner plate"></div><div class="lot-tag">100</div><h3>STEAK DINNER</h3><p>Steak Dinner for 4 at ACME steakhouse. Excludes drinks &amp; gratuity cap of $150</p><div class="btn start">STARTING : $75</div><div class="value btn-outline">VALUE : $150</div></div>
  <div class="abs lot" style="left:615px;top:1748px"><div class="lot-photo" role="img" aria-label="Steak dinner plate"></div><div class="lot-tag">100</div><h3>STEAK DINNER</h3><p>Steak Dinner for 4 at ACME steakhouse. Excludes drinks &amp; gratuity cap of $150</p><div class="btn start">STARTING : $75</div><div class="value btn-outline">VALUE : $150</div></div>
  <div class="abs lot" style="left:115px;top:1837px"><div class="lot-photo" role="img" aria-label="Steak dinner plate"></div><div class="lot-tag">100</div><h3>STEAK DINNER</h3><p>Steak Dinner for 4 at ACME steakhouse. Excludes drinks &amp; gratuity cap of $150</p><div class="btn start">STARTING : $75</div><div class="value btn-outline">VALUE : $150</div></div>
  <div class="abs lot" style="left:615px;top:1837px"><div class="lot-photo" role="img" aria-label="Steak dinner plate"></div><div class="lot-tag">100</div><h3>STEAK DINNER</h3><p>Steak Dinner for 4 at ACME steakhouse. Excludes drinks &amp; gratuity cap of $150</p><div class="btn start">STARTING : $75</div><div class="value btn-outline">VALUE : $150</div></div>
  <div class="abs lot" style="left:115px;top:1926px"><div class="lot-photo" role="img" aria-label="Steak dinner plate"></div><div class="lot-tag">100</div><h3>STEAK DINNER</h3><p>Steak Dinner for 4 at ACME steakhouse. Excludes drinks &amp; gratuity cap of $150</p><div class="btn start">STARTING : $75</div><div class="value btn-outline">VALUE : $150</div></div>
  <div class="abs lot" style="left:615px;top:1926px"><div class="lot-photo" role="img" aria-label="Steak dinner plate"></div><div class="lot-tag">100</div><h3>STEAK DINNER</h3><p>Steak Dinner for 4 at ACME steakhouse. Excludes drinks &amp; gratuity cap of $150</p><div class="btn start">STARTING : $75</div><div class="value btn-outline">VALUE : $150</div></div>
  <div class="abs lot" style="left:115px;top:2015px"><div class="lot-photo" role="img" aria-label="Steak dinner plate"></div><div class="lot-tag">100</div><h3>STEAK DINNER</h3><p>Steak Dinner for 4 at ACME steakhouse. Excludes drinks &amp; gratuity cap of $150</p><div class="btn start">STARTING : $75</div><div class="value btn-outline">VALUE : $150</div></div>
  <div class="abs lot" style="left:615px;top:2015px"><div class="lot-photo" role="img" aria-label="Steak dinner plate"></div><div class="lot-tag">100</div><h3>STEAK DINNER</h3><p>Steak Dinner for 4 at ACME steakhouse. Excludes drinks &amp; gratuity cap of $150</p><div class="btn start">STARTING : $75</div><div class="value btn-outline">VALUE : $150</div></div>
  <div class="abs lot" style="left:115px;top:2104px"><div class="lot-photo" role="img" aria-label="Steak dinner plate"></div><div class="lot-tag">100</div><h3>STEAK DINNER</h3><p>Steak Dinner for 4 at ACME steakhouse. Excludes drinks &amp; gratuity cap of $150</p><div class="btn start">STARTING : $75</div><div class="value btn-outline">VALUE : $150</div></div>
  <div class="abs lot" style="left:615px;top:2104px"><div class="lot-photo" role="img" aria-label="Steak dinner plate"></div><div class="lot-tag">100</div><h3>STEAK DINNER</h3><p>Steak Dinner for 4 at ACME steakhouse. Excludes drinks &amp; gratuity cap of $150</p><div class="btn start">STARTING : $75</div><div class="value btn-outline">VALUE : $150</div></div>
</section>

<section>
  <h2 class="abs center section-title" style="top:2246px">Event Details</h2>
  <div class="abs center brandmark" style="top:2372px"><i class="dot"></i><span>Brighter Paths</span></div>
  <p class="abs section-sub" style="left:380px;top:2419px;width:440px;text-align:center;line-height:17px;color:#555">Lorem ipsum dolor sit amet, consectetur adipisicing elit, sed do eiusmod tempor incididunt ut labore et dolore magna aliqua. Ut enim ad minim veniam, quis</p>

  <div class="abs col" style="left:81px;top:2506px;width:330px">
    <h4>Where &amp; When</h4>
    <p><b>DATE :</b> Saturday, March 23, 2019<br>
    <b>LOCATION :</b> Cedar Bend Country Club<br>
    1450 Cedar Bend Rd, Lakeview Township, MI 48000<br>
    <b>PRICE :</b> $125 per Guest<br>
    <b>DRESS :</b> Cocktail Attire – No Denim Please<br><br>
    * Be there at 5:30pm for the Pregame Warm up and Silent Auction<br><br>
    * Championship Party will include Live Auction and Award Winning Dinner<br><br>
    * Advance Online Ticket Purchase required by March 8, 2019</p>
  </div>

  <div class="abs col about" style="left:438px;top:2506px;width:325px">
    <h4>About Our Event</h4>
    <p>The premier fundraising event for Halden Hill School, PRISM Auction features outstanding live and silent auction items in a captivating environment. Attendees enjoy a great event while strengthening their bond with the school community. For Halden Hill families, friends of the school, anyone who wants to make a difference for some incredible students, participating in the PRISM Auction is a perfect way to support Halden Hill today and into the future.<br><br>
    This “party with a purpose” is an evening of celebration and community. Proceeds benefit the Odette Farrow Financial Aid Grant Award Program and professional Development for Halden Hill faculty and staff.</p>
  </div>

  <div class="abs col" style="left:796px;top:2506px;width:330px">
    <h4>Steering Commitee</h4>
    <p><b>HONORARY HOSTS :</b><br>
    Warren &amp; Lena Ostby<br>
    Dorian &amp; Celia Pruett<br><br>
    <b>AUCTION CHAIR :</b><br>
    Nora Quell<br><br>
    <b>COMMITTEE :</b><br>
    Anna Treml, Kelsey Dorn, Maren Yule, Tessa Brody,<br>
    Ivy Castell, Paula Wrenn, Dina Sorrell<br>
    Greta Hale, June Ostrow, Rita Vale</p>
  </div>
</section>

<footer>
  <div class="abs footer"></div>
  <div class="abs social" style="left:254px;top:2997px">
    <span>workroster</span><span>reelbox</span><span>chirpline</span><span>chumwall</span>
  </div>
  <div class="abs" style="left:500px;top:2988px;width:200px;display:flex;align-items:center;justify-content:center;gap:8px">
    <i style="width:22px;height:22px;border-radius:50%;background:#4a7fc1;display:block"></i>
    <span style="font-size:30px;font-weight:400;color:#4a7fc1">BidHarbor</span>
  </div>
  <div class="abs center" style="top:3041px;font-size:8px;font-weight:800;letter-spacing:1px;color:#4a7fc1">POWERED BY BIDHARBOR MOBILE BIDDING</div>
  <p class="abs" style="left:796px;top:2993px;width:260px;font-size:11px;line-height:20px;color:var(--link)">For questions, please contact Dale Fenwick at<br>dale@bidharbor.example</p>
</footer>

</body>
</html>
```